Flyer-Design für Brick and Stone Restorator
Zielgruppe
Wir sind Sydneys führender Brick and Stone Restorator.
Aufgabenstellung
Unsere neue webseite geht in ein paar tagen online und wir möchten gerne passenden zur neuen Webseite ein corporate Flyer, letztendlich soll es ein Print Version von unserer neuen Webseite sein. Sprich die wichtigsten Informationen der Webseite soll in dem Flyer enthalten sein. Letztendlich möchte ich designer keine großen einschränkungen geben, weil das ist euer job kreativ sein ;), aber der flyer sollte evtl. so aufgebaut sein das am Ende die leute entweder uns anrufen oder doch auf unsere neue Webseite gehen sprich evtl ein QR- code or what ever.
Unsere Domain ist kestrelvale.com.au, aber damit ihr die neue Webseite schon sehen könnt müsst ihr auf kestrelvale.com.au/ new, falls dieser Link nicht mehr funktionieren sollte, ist sie schon auf der richtigen domain hochgeladen.
Falls ihr irgendwelche Logos Bilder oder sonst was benötigt und diese nicht aus der Webseite entnehmen könnt, schickt einfach eine kurze Naricht, ich beantworte diese so schnell wie möglich ;)
der Flyer soll ein 6 pager sein!!
mit freundlichen Grüßen euer Kestrel Vale Team

```html
<!DOCTYPE html>
<html lang="en">
<head>
<meta charset="utf-8">
<title>Kestrel Vale – Brochure Inner Spread</title>
<link href="https://fonts.googleapis.com/css2?family=Source+Sans+3:wght@400;600;700&display=swap" rel="stylesheet">
<style>
  :root {
    --plum: #322a55;
    --plum-soft: #4a4270;
    --panel-bg: #dcdce3;
    --panel-fade: #c9c8d2;
    --ink: #2e2650;
    --photo-brick: #8a4a36;
    --photo-sand: #c08a55;
    --photo-sky: #8fb4d8;
    --photo-leaf: #5f8a3e;
  }
  * { box-sizing: border-box; margin: 0; padding: 0; }
  html, body { width: 1200px; height: 857px; overflow: hidden; background: #ececec; }
  body { font-family: "Source Sans 3", "Myriad Pro", sans-serif; color: var(--ink); }

  .spread { display: flex; width: 1200px; height: 857px; }
  .panel {
    position: relative; width: 400px; height: 857px;
    background: linear-gradient(180deg, var(--panel-bg) 0%, var(--panel-fade) 100%);
    border-right: 1px solid rgba(0,0,0,.08);
    overflow: hidden;
  }
  .panel:last-child { border-right: none; }
  .panel__header {
    height: 175px; background: var(--plum);
    display: flex; align-items: center; justify-content: center;
  }
  .panel__title { color: #fff; font-weight: 600; font-size: 26px; letter-spacing: .5px; }
  .panel__footer { position: absolute; left: 0; right: 0; bottom: 0; height: 95px; background: var(--plum); }

  .backdrop {
    position: absolute; left: 0; right: 0; top: 420px; bottom: 95px;
    background: linear-gradient(180deg, rgba(201,200,210,0) 0%, rgba(170,168,182,.45) 60%, rgba(190,180,170,.5) 100%);
  }

  /* Services */
  .services { position: relative; list-style: none; padding: 28px 30px 0 40px; }
  .service { display: flex; align-items: center; gap: 18px; height: 53px; }
  .service__icon { flex: 0 0 44px; height: 30px; border-radius: 4px; background: var(--plum); opacity: .9; }
  .service__name { font-weight: 600; font-size: 17px; line-height: 1.15; }

  /* About */
  .about { position: relative; padding: 26px 34px 0; font-size: 12.5px; line-height: 1.35; }
  .about__heading { text-align: center; font-weight: 700; font-size: 15px; margin-bottom: 10px; }
  .about p { margin-bottom: 9px; text-align: justify; }
  .about strong { font-weight: 600; }
  .brand { display: flex; align-items: center; justify-content: center; gap: 10px; margin: 18px 0 16px; }
  .brand__mark { width: 22px; height: 22px; background: var(--plum); }
  .brand__name { font-weight: 700; font-size: 30px; color: var(--plum); letter-spacing: 1px; }

  /* Gallery */
  .gallery { position: absolute; left: 0; top: 175px; right: 0; bottom: 95px; }
  .photo { position: absolute; border-radius: 2px; }
  .photo--a { left: 40px;  top: 30px;  width: 160px; height: 90px;  background: linear-gradient(135deg, var(--photo-sand), var(--photo-sky)); }
  .photo--b { left: 20px;  top: 150px; width: 195px; height: 180px; background: linear-gradient(160deg, var(--photo-sky), var(--photo-brick) 55%); }
  .photo--c { left: 225px; top: 115px; width: 160px; height: 190px; background: linear-gradient(150deg, var(--photo-sand), #a8683f); }
  .photo--d { left: 30px;  top: 355px; width: 150px; height: 100px; background: linear-gradient(180deg, var(--photo-leaf), var(--photo-brick) 60%); }
  .photo--e { left: 215px; top: 325px; width: 150px; height: 110px; background: linear-gradient(180deg, var(--photo-sky), var(--photo-brick) 50%); }
  .photo--f { left: 30px;  top: 475px; width: 150px; height: 100px; background: linear-gradient(150deg, #9a5443, #d9d4cc); }
  .photo--g { left: 195px; top: 450px; width: 180px; height: 135px; background: linear-gradient(180deg, var(--photo-brick), #6d3b2c 60%, var(--photo-leaf)); }
</style>
</head>
<body>
<main class="spread">

  <section class="panel panel--services">
    <div class="backdrop" role="img" aria-label="Faded harbour city skyline photograph"></div>
    <header class="panel__header"><h2 class="panel__title">Our Services</h2></header>
    <ul class="services">
      <li class="service"><span class="service__icon" role="img" aria-label="Brick stack icon"></span><span class="service__name">Brick &amp; Stone Repointing</span></li>
      <li class="service"><span class="service__icon" role="img" aria-label="Mortar joint icon"></span><span class="service__name">Tuckpointing</span></li>
      <li class="service"><span class="service__icon" role="img" aria-label="Trowel icon"></span><span class="service__name">Restoring Brick and Stone</span></li>
      <li class="service"><span class="service__icon" role="img" aria-label="Arched window icon"></span><span class="service__name">Lintel and Arch Bar Replacement</span></li>
      <li class="service"><span class="service__icon" role="img" aria-label="Brick wall with tick icon"></span><span class="service__name">Remedial Wall Tie Replacement and Installation</span></li>
      <li class="service"><span class="service__icon" role="img" aria-label="Toolbox icon"></span><span class="service__name">Damp Proof Course and Flashing Replacement &amp; Installation</span></li>
      <li class="service"><span class="service__icon" role="img" aria-label="Wrench icon"></span><span class="service__name">Ventilation Replacement &amp; Installation</span></li>
      <li class="service"><span class="service__icon" role="img" aria-label="Water drops icon"></span><span class="service__name">Water Repellant</span></li>
      <li class="service"><span class="service__icon" role="img" aria-label="Scaffolding icon"></span><span class="service__name">Scaffolding Service</span></li>
    </ul>
    <footer class="panel__footer"></footer>
  </section>

  <section class="panel panel--about">
    <div class="backdrop" role="img" aria-label="Faded harbour bridge photograph"></div>
    <header class="panel__header"><h2 class="panel__title">About Us</h2></header>
    <div class="about">
      <h3 class="about__heading">Who we service</h3>
      <p><strong>Strata &amp; Owner Corporations:</strong> Kestrel Vale can work alongside and coordinate with industry professionals alike to deliver an exceptional brick restoration or repair project with full legislative compliance.</p>
      <p><strong>Residential &amp; Commercial Buildings:</strong> Owners of residential and commercial brick buildings can rely on our high standard of professionalism, service and careful tenant consideration to complete any size project.</p>
      <p><strong>Heritage Associations:</strong> Various remedial techniques, attention to detail, patience and experience enables Kestrel Vale to provide Heritage projects with the respect and integrity they deserve.</p>
      <div class="brand"><span class="brand__mark"></span><span class="brand__name">KESTREL VALE</span></div>
      <h3 class="about__heading">Why choose KESTREL VALE?</h3>
      <p><strong>Commitment:</strong> The Kestrel Vale team are committed to helping you maintain the integrity of your home or building facade.</p>
      <p><strong>Quality:</strong> Our experienced team and continuing professional development ensure we can deliver a High Standard of Quality &amp; Service.</p>
      <p><strong>Experience:</strong> With experience ranging from restoring the Harbourline Metro railway network, to restoring a multi storey heritage building in the heart of Sydney, we are the best.</p>
    </div>
    <footer class="panel__footer"></footer>
  </section>

  <section class="panel panel--gallery">
    <div class="backdrop" role="img" aria-label="Faded city skyline photograph"></div>
    <header class="panel__header"><h2 class="panel__title">Gallery</h2></header>
    <div class="gallery">
      <div class="photo photo--a" role="img" aria-label="Photo of a restored sandstone apartment block"></div>
      <div class="photo photo--b" role="img" aria-label="Photo of a red brick building with arched window"></div>
      <div class="photo photo--c" role="img" aria-label="Photo of a tan brick wall with windows"></div>
      <div class="photo photo--d" role="img" aria-label="Photo of a brick garden wall with hedge"></div>
      <div class="photo photo--e" role="img" aria-label="Photo of a red brick tower against sky"></div>
      <div class="photo photo--f" role="img" aria-label="Photo of a multi storey brick apartment building"></div>
      <div class="photo photo--g" role="img" aria-label="Photo of a brick facade with window and shrubs"></div>
    </div>
    <footer class="panel__footer"></footer>
  </section>

</main>
</body>
</html>
```